Redesign of existing business card

I would like the "signage" attachment converted into a business card. This needs to be double sided aswell, keeping the phone number and names on the front, and the email + website on the back.

Second attachment is the current business card design.

Larger font for contact details is required.

Must keep to original color themes (electric blue, silver/grey etc)

Back of the card to have blue background with white writing.

Industry/Entity Type

Business

Contact Information for Business Card

Refer to existing design from attachments

Requirements
Must have
• Refer to existing design from attachments
Nice to have

```html
<!DOCTYPE html>
<html lang="en">
<head>
<meta charset="utf-8">
<title>Volta Line Electrical – Business Card</title>
<link href="https://fonts.googleapis.com/css2?family=Exo+2:wght@300;400;600;700&display=swap" rel="stylesheet">
<style>
  :root {
    --electric-blue: #3d5aab;
    --silver: #c9cbcf;
    --silver-dark: #9a9da3;
    --grey-text: #8a8c90;
    --card-white: #ffffff;
    --clear-tone-light: #e6cfae;
    --clear-tone-dark: #c99e6c;
    --canvas: #ecebe8;
  }
  * { margin: 0; padding: 0; box-sizing: border-box; }
  html, body {
    width: 1189px; height: 1200px; overflow: hidden;
    background: var(--canvas);
    font-family: "Exo 2", sans-serif;
  }
  .canvas { position: relative; width: 1189px; height: 1200px; }

  .card {
    position: absolute;
    width: 763px; height: 435px;
    background: var(--card-white);
    overflow: hidden;
    box-shadow: 0 6px 18px rgba(0,0,0,0.12);
  }
  .card--back  { left: 316px; top: 130px; background: var(--electric-blue); }
  .card--front { left: 121px; top: 645px; }

  .card__art { position: absolute; inset: 0; width: 100%; height: 100%; }

  /* Back */
  .tagline {
    position: absolute; right: 36px; top: 58px;
    text-align: right;
    color: var(--card-white);
    font-weight: 700; font-size: 29px; line-height: 36px;
    text-transform: uppercase;
  }
  .contact-list {
    position: absolute; right: 35px; top: 250px;
    list-style: none; text-align: right;
  }
  .contact-list li {
    display: flex; justify-content: flex-end; align-items: center; gap: 8px;
    color: var(--card-white);
    font-weight: 400; font-size: 21px; line-height: 28px;
  }
  .icon-box {
    width: 23px; height: 23px; border-radius: 3px;
    background: var(--card-white);
    display: inline-flex; align-items: center; justify-content: center;
  }
  .icon-box--blue { background: var(--electric-blue); }

  .brand {
    position: absolute;
    display: flex; align-items: center; gap: 12px;
    color: var(--electric-blue);
    font-weight: 700; text-transform: uppercase;
  }
  .brand__dot {
    border-radius: 50%;
    background: var(--electric-blue);
    flex: none;
  }
  .brand__name { line-height: 1; letter-spacing: 1px; }
  .brand--small { right: 36px; top: 352px; font-size: 26px; color: var(--card-white); }
  .brand--small .brand__dot { width: 50px; height: 50px; background: var(--card-white); }
  .brand--large { left: 39px; top: 72px; font-size: 36px; gap: 14px; }
  .brand--large .brand__dot { width: 76px; height: 76px; }

  /* Front */
  .person { position: absolute; left: 39px; top: 294px; }
  .person__name {
    color: var(--electric-blue);
    font-weight: 700; font-size: 27px; line-height: 32px;
  }
  .person__role {
    color: var(--grey-text);
    font-weight: 300; font-size: 20px; line-height: 26px;
  }
  .phone {
    position: absolute; left: 39px; top: 375px;
    display: flex; align-items: center; gap: 8px;
    color: var(--grey-text);
    font-weight: 300; font-size: 21px;
  }
</style>
</head>
<body>
<main class="canvas">

  <section class="card card--back" aria-label="Card back">
    <svg class="card__art" viewBox="0 0 763 435" aria-hidden="true">
      <defs>
        <linearGradient id="clearToneBack" x1="0" y1="0" x2="1" y2="1">
          <stop offset="0" stop-color="var(--clear-tone-light)"/>
          <stop offset="1" stop-color="var(--clear-tone-dark)"/>
        </linearGradient>
      </defs>
      <polygon points="0,0 88,0 308,435 0,435" fill="url(#clearToneBack)"/>
      <circle cx="206" cy="213" r="188" fill="none" stroke="var(--silver)" stroke-width="24"/>
    </svg>

    <h2 class="tagline">Your trusted<br>electrical<br>contractor</h2>

    <ul class="contact-list">
      <li>daniel@voltaline.com
        <span class="icon-box">
          <svg width="15" height="11" viewBox="0 0 15 11"><rect x="0.75" y="0.75" width="13.5" height="9.5" fill="none" stroke="#3d5aab" stroke-width="1.5"/><polyline points="1,1 7.5,6 14,1" fill="none" stroke="#3d5aab" stroke-width="1.5"/></svg>
        </span>
      </li>
      <li>www.voltaline.com.au
        <span class="icon-box">
          <svg width="15" height="15" viewBox="0 0 15 15" fill="none" stroke="#3d5aab" stroke-width="1.2"><circle cx="7.5" cy="7.5" r="6.5"/><ellipse cx="7.5" cy="7.5" rx="3" ry="6.5"/><line x1="1" y1="7.5" x2="14" y2="7.5"/></svg>
        </span>
      </li>
    </ul>

    <div class="brand brand--small">
      <span class="brand__dot"></span>
      <span class="brand__name">Volta Line<br>Electrical</span>
    </div>
  </section>

  <section class="card card--front" aria-label="Card front">
    <svg class="card__art" viewBox="0 0 763 435" aria-hidden="true">
      <defs>
        <linearGradient id="clearToneFront" x1="0" y1="0" x2="1" y2="1">
          <stop offset="0" stop-color="var(--clear-tone-light)"/>
          <stop offset="1" stop-color="var(--clear-tone-dark)"/>
        </linearGradient>
      </defs>
      <polygon points="676,0 763,0 763,435 454,435" fill="url(#clearToneFront)"/>
      <circle cx="565" cy="215" r="190" fill="none" stroke="var(--silver)" stroke-width="24"/>
    </svg>

    <div class="brand brand--large">
      <span class="brand__dot"></span>
      <span class="brand__name">Volta Line<br>Electrical</span>
    </div>

    <div class="person">
      <h1 class="person__name">Daniel Reeve</h1>
      <p class="person__role">Director</p>
    </div>

    <p class="phone">
      <span class="icon-box icon-box--blue">
        <svg width="13" height="15" viewBox="0 0 13 15"><path d="M3 1 L5 4.5 L3.6 6 C4.4 8 5.6 9.5 7.4 10.6 L9 9.3 L12 11.5 L10.5 14 C5.5 13.5 1 8.5 1 2.5 Z" fill="#fff"/></svg>
      </span>
      0400 555 019
    </p>
  </section>

</main>
</body>
</html>
```